Layout für Longboardshop
Zielgruppe
Online Shop für Longboards, basierend auf Kassalo 4.1.2
Zielgruppe: Sportliche Menschen mit Hang zum Wellenreiten, Surfen,Kiten, Snowboarden oder Skateboarden.
Aufgabenstellung
Erstellung des Grunddesigns (Header, Footer, Menü, Detailansicht, Buttons) als PSD. Die Umsetzung in ein Template erledigen wir alleine.
Neugründung: Es existieren noch keine Logos oder Farbvorgaben.
We have no site, it is a completly new project. There are no limits concerning colors, fonts etc.
Competitors:
http://www.brettgleiter-zone.de
http://fenwick-rollbretter.de/
http://www.rollbrettladen.de/
http://www.kerbo.de/de_DE/Skateboard/Longboards.html?sid=1
http://www.pumeri-boards.de/
I think, big pictures transporting the surfstyle attitude of this sport works good.
Der Grundaufbau sollte sich an http://www.kassalodemo.de/ anlehnen, um den Anpassungsaufwand mgl. überschaubar zu halten.

```html
<!DOCTYPE html>
<html lang="de">
<head>
<meta charset="utf-8">
<title>Rollwerk Shop – Decks</title>
<link rel="stylesheet" href="https://fonts.googleapis.com/css2?family=Bebas+Neue&family=Open+Sans:wght@400;600;700&family=Arimo:wght@400;700&display=swap">
<style>
:root{
  --dark:#172a33;
  --darker:#122129;
  --ink:#0f0f10;
  --blue:#1ec0ee;
  --paper:#f1f1f1;
  --white:#ffffff;
  --grey:#8a8f92;
  --text:#222;
  --fb:#2c3e6e;
}
*{margin:0;padding:0;box-sizing:border-box}
html,body{width:1200px;height:1119px;overflow:hidden}
body{position:relative;background:repeating-linear-gradient(135deg,#f4f4f4 0 3px,#ebebeb 3px 5px);font-family:"Open Sans",sans-serif;color:var(--text)}
.abs{position:absolute}
.topbar{left:0;top:0;width:1200px;height:27px;background:var(--dark);color:var(--white);font-size:9px;font-weight:600}
.topbar .item{position:absolute;top:0;height:27px;line-height:27px;padding:0 12px;border-right:1px solid #2b3f49;display:flex;align-items:center;gap:5px}
.topbar .welcome{position:absolute;right:228px;top:0;line-height:27px}
.logo{left:294px;top:50px;font-family:"Arimo",sans-serif;font-size:38px;color:var(--blue);letter-spacing:-1px;display:flex;align-items:center;gap:8px}
.logo .dot{width:10px;height:10px;background:var(--blue)}
.nav{left:299px;top:117px;width:672px;height:33px;background:var(--dark);display:flex;font-family:"Arimo",sans-serif;font-size:13.5px;color:var(--white)}
.nav a{position:relative;display:flex;align-items:center;justify-content:center;gap:7px;border-right:1px solid #22363f;color:inherit;text-decoration:none}
.nav a::after{content:"";position:absolute;right:2px;bottom:2px;border-left:4px solid transparent;border-bottom:4px solid var(--blue)}
.nav a.active{color:var(--blue)}
.catmenu{left:299px;top:156px;width:173px;background:var(--dark);list-style:none;font-family:"Arimo",sans-serif;font-size:12px;color:var(--white)}
.catmenu li{height:25px;line-height:25px;padding-left:27px;border-bottom:1px solid #0f1d23;position:relative}
.catmenu li::before{content:"";position:absolute;left:10px;top:9px;border-left:6px solid var(--white);border-top:4px solid transparent;border-bottom:4px solid transparent}
.catmenu li.active{color:var(--blue)}
.hero{left:472px;top:156px;width:500px;height:213px;background:linear-gradient(180deg,#8fd0f0 0%,#c9dbe0 45%,#b5aba0 70%,#8d8782 100%)}
.search-tab{left:802px;top:191px;width:182px;height:16px;background:var(--blue);color:var(--white);font-family:"Bebas Neue",sans-serif;font-size:12px;line-height:17px;padding-left:8px;letter-spacing:.4px}
.search-box{left:701px;top:206px;width:283px;height:40px;background:var(--blue)}
.search-box input{position:absolute;left:15px;top:8px;width:251px;height:24px;border:0;padding-left:6px;font:9px "Open Sans",sans-serif;color:#888}
.bestseller{left:299px;top:331px;width:173px;height:208px;background:linear-gradient(180deg,#202226,#0e0f11)}
.bestseller h2{position:absolute;left:8px;top:9px;font-family:"Bebas Neue",sans-serif;font-weight:400;font-size:20px;line-height:21px;color:var(--white)}
.bestseller h2 span{display:block;padding-left:47px}
.bestseller .photo{position:absolute;left:30px;top:66px;width:118px;height:110px;background:radial-gradient(circle,#cdb57a,#5a4a2a 70%,transparent 72%)}
.cartbtn{width:23px;height:21px;background:var(--blue);display:flex;align-items:center;justify-content:center}
.social{left:299px;top:539px;width:174px;height:33px;background:var(--fb)}
.social .sq{position:absolute;left:0;top:0;width:35px;height:33px;background:#3a4f86}
.social .like{position:absolute;left:45px;top:11px;font-size:6px;color:var(--fb);display:flex;gap:3px}
.social .like span{background:#eef1f7;padding:1px 4px;border:1px solid #c9d0e0}
.promo{left:299px;top:572px;width:173px;height:364px;background:var(--ink);color:var(--white);text-align:center}
.promo .brand{position:absolute;top:90px;width:100%;font-family:"Arimo",sans-serif;font-weight:700;font-size:15px;letter-spacing:2px}
.promo .slogan{position:absolute;top:140px;width:100%;font-family:"Bebas Neue",sans-serif;font-size:13px}
.newsletter{left:286px;top:804px;width:187px;height:125px;background:var(--blue);color:var(--white);padding:6px 8px}
.newsletter h2{font-family:"Bebas Neue",sans-serif;font-weight:400;font-size:21px;line-height:24px}
.newsletter p{font-size:7.4px;line-height:12.4px;margin-top:4px}
.newsletter input{position:absolute;left:8px;top:89px;width:170px;height:23px;border:0;padding-left:9px;font:7.4px "Open Sans",sans-serif;color:#888}
.products{left:473px;top:369px;width:498px;height:567px;background:var(--white)}
.card{position:absolute;width:150px}
.card .shot{height:69px;width:120px;margin-left:4px}
.shot.silver{background:linear-gradient(160deg,#e6e6e6,#8b8b8b 55%,#f7f7f7)}
.shot.white{background:linear-gradient(160deg,#f2f2f2,#3d3d3d 60%,#fafafa)}
.shot.black{background:linear-gradient(160deg,#eee,#2a2a2a 55%,#7bb43c 62%,#f5f5f5)}
.card h3{margin-top:13px;font-size:10.5px;font-weight:700;letter-spacing:.6px;color:#1b1b1b}
.card p{font-size:8px;line-height:10px;color:var(--grey);margin-top:5px}
.card .buy{position:relative;height:28px;margin-top:7px}
.card .price{position:absolute;left:0;top:0;font-weight:700;font-size:10.5px}
.card .basket{position:absolute;left:55px;top:0;width:29px;height:28px;background:var(--dark);display:flex;align-items:center;justify-content:center}
.card .details{position:absolute;left:84px;top:0;width:50px;height:19px;background:var(--blue);color:var(--white);font-size:8.4px;font-weight:700;text-align:center;line-height:19px;letter-spacing:.4px}
.vline{position:absolute;width:1px;background:#e3e3e3}
.hline{position:absolute;left:14px;width:470px;height:1px;background:#e3e3e3}
.footer{left:299px;top:936px;width:672px;height:183px;background:var(--dark);border-top:3px solid var(--blue);color:var(--white)}
.fcol{position:absolute;top:20px;width:138px}
.fcol h4{font-size:11.5px;font-weight:600;padding-bottom:4px;border-bottom:1px solid #2c424c}
.fcol ul{list-style:none;margin-top:8px;font-size:7px;font-weight:600}
.fcol li{height:14.4px;padding-left:7px;position:relative}
.fcol li::before{content:"";position:absolute;left:0;top:4px;width:2px;height:2px;background:var(--blue)}
.footer .bottom{position:absolute;left:0;top:148px;width:672px;height:32px;border-top:1px solid #22363f;font-size:7px;font-weight:600}
.footer .bottom .copy{position:absolute;left:16px;top:12px}
.footer .bottom .legal{position:absolute;right:15px;top:12px}
</style>
</head>
<body>
<header>
  <div class="abs topbar">
    <div class="item" style="left:286px"><svg width="9" height="8" viewBox="0 0 10 9"><path d="M5 9 0 4A2.6 2.6 0 0 1 5 1.2 2.6 2.6 0 0 1 10 4Z" fill="#fff"/></svg>Wunschzettel</div>
    <div class="item" style="left:384px"><svg width="8" height="9" viewBox="0 0 8 9"><circle cx="4" cy="2.4" r="2.2" fill="#fff"/><path d="M0 9C0 5 8 5 8 9Z" fill="#fff"/></svg>Benutzerkonto</div>
    <div class="item" style="left:487px"><svg width="11" height="9" viewBox="0 0 11 9"><path d="M0 1h2l2 5h6l1-4H3" stroke="#fff" fill="none"/><circle cx="4.5" cy="8" r="1" fill="#fff"/><circle cx="9" cy="8" r="1" fill="#fff"/></svg>Warenkorb</div>
    <div class="welcome">Willkommen auf www.Rollwerk-Shop24.de - shop slogan here</div>
  </div>
  <div class="abs logo"><span>Rollwerk</span><span class="dot"></span></div>
  <nav class="abs nav">
    <a style="width:109px"><svg width="12" height="11" viewBox="0 0 12 11"><path d="M6 0 0 5.5h2V11h3V7h2v4h3V5.5h2Z" fill="#fff"/></svg>Startseite</a>
    <a style="width:103px">Longboards</a>
    <a class="active" style="width:71px">Decks</a>
    <a style="width:75px">Achsen</a>
    <a style="width:97px">Kugellager</a>
    <a style="width:83px">Weheels</a>
    <a style="width:134px;justify-content:flex-start;padding-left:19px">Zubehör</a>
  </nav>
</header>

<aside>
  <ul class="abs catmenu">
    <li class="active">Alle Decks</li>
    <li>Vexo Decks</li>
    <li>Tannel Decks</li>
    <li>Orbis Decks</li>
    <li>Kalumo Bay Decks</li>
    <li>Heedfree Decks</li>
    <li>Velmo Decks</li>
  </ul>
  <section class="abs bestseller">
    <h2>Bestseller<span>des Monats</span></h2>
    <div class="photo" role="img" aria-label="Foto: Longboard-Slidehandschuhe in Beige und Schwarz"></div>
    <div class="cartbtn" style="position:absolute;left:138px;top:175px"><svg width="11" height="9" viewBox="0 0 11 9"><path d="M0 3h11L9.5 9h-8Z M3 3 5.5 0 8 3" fill="none" stroke="#fff" stroke-width="1.3"/></svg></div>
  </section>
  <div class="abs social">
    <div class="sq"></div>
    <div class="like"><span>Gefällt mir</span><span>1,5 Mio.</span></div>
  </div>
  <section class="abs promo">
    <div class="brand">VELOCE</div>
    <div class="slogan">Ride on. !</div>
  </section>
  <section class="abs newsletter">
    <h2>Newsletter</h2>
    <p>Lorem ipsum dolor sit amet, consetetur sadip­scing elitr, sed diam nonumy eirmod tempor invidunt. em ipsum dolor sit amet, consetetur sadipscing elitr, sed diam n</p>
    <input type="text" placeholder="E-Mail Adresse eingeben">
  </section>
</aside>

<main>
  <div class="abs hero" role="img" aria-label="Foto: Longboard in Bodennähe mit grünen Rollen auf sonniger Straße, Häuser und blauer Himmel im Hintergrund"></div>
  <div class="abs search-tab">Longboardshop durchsuchen</div>
  <div class="abs search-box"><input type="text" placeholder="Suchbegriff hier eingeben..."></div>

  <section class="abs products">
    <div class="vline" style="left:170px;top:13px;height:159px"></div>
    <div class="vline" style="left:338px;top:13px;height:159px"></div>
    <div class="hline" style="top:187px"></div>
    <div class="vline" style="left:170px;top:203px;height:159px"></div>
    <div class="vline" style="left:338px;top:203px;height:159px"></div>
    <div class="hline" style="top:378px"></div>
    <div class="vline" style="left:170px;top:399px;height:159px"></div>
    <div class="vline" style="left:338px;top:399px;height:159px"></div>

    <!-- row 1 -->
    <article class="card" style="left:14px;top:13px"><div class="shot silver" role="img" aria-label="Produktfoto: silberne Longboard-Achse"></div><h3>TILTA INVERTED</h3><p>Lorem ipsum dolor sit amet, con-setetur sadipscing.</p><div class="buy"><span class="price">55,00 €*</span><span class="basket"><svg width="13" height="11" viewBox="0 0 11 9"><path d="M0 3h11L9.5 9h-8Z M3 3 5.5 0 8 3" fill="none" stroke="#fff" stroke-width="1.3"/></svg></span><span class="details">DETAILS</span></div></article>
    <article class="card" style="left:181px;top:13px"><div class="shot white" role="img" aria-label="Produktfoto: weiße Longboard-Achse"></div><h3>ORBIS TILTA BEST</h3><p>Lorem ipsum dolor sit amet, con-setetur sadipscing.</p><div class="buy"><span class="price">98,00 €*</span><span class="basket"><svg width="13" height="11" viewBox="0 0 11 9"><path d="M0 3h11L9.5 9h-8Z M3 3 5.5 0 8 3" fill="none" stroke="#fff" stroke-width="1.3"/></svg></span><span class="details">DETAILS</span></div></article>
    <article class="card" style="left:349px;top:13px"><div class="shot black" role="img" aria-label="Produktfoto: schwarze Longboard-Achse"></div><h3>BRUMMAR RIDGE</h3><p>Lorem ipsum dolor sit amet, con-setetur sadipscing.</p><div class="buy"><span class="price">89,00 €*</span><span class="basket"><svg width="13" height="11" viewBox="0 0 11 9"><path d="M0 3h11L9.5 9h-8Z M3 3 5.5 0 8 3" fill="none" stroke="#fff" stroke-width="1.3"/></svg></span><span class="details">DETAILS</span></div></article>

    <!-- row 2 -->
    <article class="card" style="left:14px;top:203px"><div class="shot silver" role="img" aria-label="Produktfoto: silberne Longboard-Achse"></div><h3>TILTA INVERTED</h3><p>Lorem ipsum dolor sit amet, con-setetur sadipscing.</p><div class="buy"><span class="price">55,00 €*</span><span class="basket"><svg width="13" height="11" viewBox="0 0 11 9"><path d="M0 3h11L9.5 9h-8Z M3 3 5.5 0 8 3" fill="none" stroke="#fff" stroke-width="1.3"/></svg></span><span class="details">DETAILS</span></div></article>
    <article class="card" style="left:181px;top:203px"><div class="shot white" role="img" aria-label="Produktfoto: weiße Longboard-Achse"></div><h3>ORBIS TILTA BEST</h3><p>Lorem ipsum dolor sit amet, con-setetur sadipscing.</p><div class="buy"><span class="price">98,00 €*</span><span class="basket"><svg width="13" height="11" viewBox="0 0 11 9"><path d="M0 3h11L9.5 9h-8Z M3 3 5.5 0 8 3" fill="none" stroke="#fff" stroke-width="1.3"/></svg></span><span class="details">DETAILS</span></div></article>
    <article class="card" style="left:349px;top:203px"><div class="shot black" role="img" aria-label="Produktfoto: schwarze Longboard-Achse"></div><h3>BRUMMAR RIDGE</h3><p>Lorem ipsum dolor sit amet, con-setetur sadipscing.</p><div class="buy"><span class="price">89,00 €*</span><span class="basket"><svg width="13" height="11" viewBox="0 0 11 9"><path d="M0 3h11L9.5 9h-8Z M3 3 5.5 0 8 3" fill="none" stroke="#fff" stroke-width="1.3"/></svg></span><span class="details">DETAILS</span></div></article>

    <!-- row 3 -->
    <article class="card" style="left:14px;top:399px"><div class="shot silver" role="img" aria-label="Produktfoto: silberne Longboard-Achse"></div><h3>TILTA INVERTED</h3><p>Lorem ipsum dolor sit amet, con-setetur sadipscing.</p><div class="buy"><span class="price">55,00 €*</span><span class="basket"><svg width="13" height="11" viewBox="0 0 11 9"><path d="M0 3h11L9.5 9h-8Z M3 3 5.5 0 8 3" fill="none" stroke="#fff" stroke-width="1.3"/></svg></span><span class="details">DETAILS</span></div></article>
    <article class="card" style="left:181px;top:399px"><div class="shot white" role="img" aria-label="Produktfoto: weiße Longboard-Achse"></div><h3>ORBIS TILTA BEST</h3><p>Lorem ipsum dolor sit amet, con-setetur sadipscing.</p><div class="buy"><span class="price">98,00 €*</span><span class="basket"><svg width="13" height="11" viewBox="0 0 11 9"><path d="M0 3h11L9.5 9h-8Z M3 3 5.5 0 8 3" fill="none" stroke="#fff" stroke-width="1.3"/></svg></span><span class="details">DETAILS</span></div></article>
    <article class="card" style="left:349px;top:399px"><div class="shot black" role="img" aria-label="Produktfoto: schwarze Longboard-Achse"></div><h3>BRUMMAR RIDGE</h3><p>Lorem ipsum dolor sit amet, con-setetur sadipscing.</p><div class="buy"><span class="price">89,00 €*</span><span class="basket"><svg width="13" height="11" viewBox="0 0 11 9"><path d="M0 3h11L9.5 9h-8Z M3 3 5.5 0 8 3" fill="none" stroke="#fff" stroke-width="1.3"/></svg></span><span class="details">DETAILS</span></div></article>
  </section>
</main>

<footer class="abs footer">
  <div class="fcol" style="left:11px"><h4>Informationen</h4><ul><li>Lorem ipsum dolorisits</li><li>Amet consecectetur adipiscing</li><li>Vivarmus</li><li>Blandid ipsum proas</li><li>Arcu nulla dignistatinias</li></ul></div>
  <div class="fcol" style="left:162px"><h4>Sitemap</h4><ul><li>Lorem ipsum dolorisits</li><li>Amet consecectetur adipiscing</li><li>Vivarmus</li><li>Blandid ipsum proas</li><li>Arcu nulla dignistatinias</li></ul></div>
  <div class="fcol" style="left:313px"><h4>Zahlungsarten</h4><ul><li>Lorem ipsum dolorisits</li><li>Amet consecectetur adipiscing</li><li>Vivarmus</li><li>Blandid ipsum proas</li><li>Arcu nulla dignistatinias</li></ul></div>
  <div class="fcol" style="left:465px"><h4>Neuigkeiten</h4><ul><li>Lorem ipsum dolorisits</li><li>Amet consecectetur adipiscing</li><li>Vivarmus</li><li>Blandid ipsum proas</li><li>Arcu nulla dignistatinias</li></ul></div>
  <div class="bottom">
    <span class="copy">© copyrights by www.beispielseite.de | all rigts reserved</span>
    <span class="legal">Impressum &nbsp;| &nbsp;Kontakt &nbsp;| AGBs</span>
  </div>
</footer>
</body>
</html>
```